New Zealand Export company needs business cards

We need new business cards to match our new logo for a company based in New Zealand who deal specifically with the Pacific Islands. We source, consolidate and ship products out of New Zealand to the Pacific Islands. Will attach our old ones and also new logo.
Would like the Islands we deal with and the areas of work we have access to, to be included on the business cards.

Contact Information for Business Card

T +64 9 571 3048
F +64 9 571 6285
12-18 Kowhai Lane, Ardmore, 2582
PO Box 814, Ardmore, Auckland 2583, New Zealand
www.falconfreight.example.nz
E sales@falconfreight.example.nz

Font styles to use
Sans Serif

Colors
85abd2
33a6d7
ffffff

Requirements
Must have
• A company of PWM

```html
<!DOCTYPE html>
<html lang="en">
<head>
<meta charset="utf-8">
<title>Falcon Freight – Business Cards</title>
<link rel="stylesheet" href="https://fonts.googleapis.com/css2?family=Arimo:wght@400;700&family=Michroma&display=swap">
<style>
  :root {
    --navy: #1b56a4;
    --sky: #33a6d7;
    --soft-blue: #85abd2;
    --paper: #ffffff;
    --backdrop-top: #2b3238;
    --backdrop-bottom: #181c20;
  }
  * { box-sizing: border-box; margin: 0; padding: 0; }
  html, body { width: 1200px; height: 1200px; overflow: hidden; }
  body {
    background: radial-gradient(circle at 50% 40%, var(--backdrop-top), var(--backdrop-bottom));
    font-family: "Arimo", Arial, sans-serif;
    position: relative;
  }
  .card {
    position: absolute;
    left: 180px;
    width: 840px;
    height: 480px;
    background: var(--paper);
    border-radius: 10px;
    box-shadow: 0 18px 40px rgba(0,0,0,.5);
    overflow: hidden;
  }
  .card--front { top: 90px; }
  .card--back { top: 630px; }

  .wordmark { display: flex; align-items: center; gap: 14px; }
  .wordmark__square { width: 34px; height: 34px; background: var(--navy); flex: none; }
  .wordmark__name {
    font-family: "Michroma", Arial, sans-serif;
    color: var(--navy);
    font-size: 30px;
    letter-spacing: 1px;
    line-height: 1.1;
    white-space: nowrap;
  }

  .card--front .wordmark { position: absolute; left: 50px; top: 262px; }
  .card--front .wordmark__square { width: 30px; height: 30px; }
  .card--front .wordmark__name { font-size: 23px; }

  .contact-rail { position: absolute; left: 460px; top: 0; width: 66px; height: 480px; }
  .rail-tab {
    position: absolute; left: 0; width: 66px;
    background: var(--sky);
    display: flex; align-items: center; justify-content: center;
    border-radius: 8px;
  }
  .rail-tab svg { width: 34px; height: 34px; }
  .rail-tab--person { top: 70px; height: 80px; }
  .rail-tab--phone { top: 168px; height: 56px; }
  .rail-tab--fax { top: 234px; height: 56px; }
  .rail-tab--mail { top: 300px; height: 56px; }
  .rail-tab--pin { top: 366px; height: 114px; border-radius: 8px 8px 0 0; align-items: flex-start; padding-top: 24px; }

  .contact-lines { position: absolute; left: 548px; top: 0; right: 24px; color: var(--navy); }
  .holder { position: absolute; top: 86px; }
  .holder__name { font-size: 26px; font-weight: 700; letter-spacing: .5px; }
  .holder__role { font-size: 15px; color: var(--sky); margin-top: 2px; }
  .contact-line { position: absolute; font-size: 19px; white-space: nowrap; }
  .contact-line--phone { top: 184px; }
  .contact-line--fax { top: 250px; }
  .contact-line--mail { top: 316px; font-size: 17px; }
  .contact-line--address { top: 382px; font-size: 14px; line-height: 1.45; white-space: normal; }

  .card--back .back-layout {
    position: absolute; inset: 0;
    display: flex; flex-direction: column; align-items: center; justify-content: center; gap: 30px;
  }
  .card--back .wordmark__square { width: 46px; height: 46px; }
  .card--back .wordmark__name { font-size: 40px; }
  .website { display: flex; align-items: center; gap: 12px; color: var(--sky); font-size: 22px; }
  .website svg { width: 28px; height: 28px; }
</style>
</head>
<body>

<section class="card card--front" aria-label="Business card front">
  <div class="wordmark">
    <span class="wordmark__square"></span>
    <span class="wordmark__name">FALCON FREIGHT</span>
  </div>

  <div class="contact-rail">
    <div class="rail-tab rail-tab--person">
      <svg viewBox="0 0 24 24" fill="#fff"><circle cx="12" cy="8" r="4.5"/><path d="M3 22c0-5 4-8 9-8s9 3 9 8z"/></svg>
    </div>
    <div class="rail-tab rail-tab--phone">
      <svg viewBox="0 0 24 24" fill="none" stroke="#fff" stroke-width="1.8"><circle cx="12" cy="12" r="10"/><path d="M8 7.5c0 5 3.5 8.5 8.5 8.5l1-2-2.5-1.2-1 1c-1.5-.6-2.7-1.8-3.3-3.3l1-1L10.5 6.5z" fill="#fff" stroke="none"/></svg>
    </div>
    <div class="rail-tab rail-tab--fax">
      <svg viewBox="0 0 24 24" fill="none" stroke="#fff" stroke-width="1.8"><rect x="3" y="9" width="18" height="10" rx="1.5"/><path d="M7 9V3h10v6M7 15h10M7 18h10"/></svg>
    </div>
    <div class="rail-tab rail-tab--mail">
      <svg viewBox="0 0 24 24" fill="none" stroke="#fff" stroke-width="1.8"><rect x="2.5" y="5" width="19" height="14"/><path d="M2.5 5l9.5 8 9.5-8M2.5 19l7-6.5M21.5 19l-7-6.5"/></svg>
    </div>
    <div class="rail-tab rail-tab--pin">
      <svg viewBox="0 0 24 24" fill="none" stroke="#fff" stroke-width="1.8"><path d="M12 21s-6-6.5-6-11a6 6 0 0 1 12 0c0 4.5-6 11-6 11z"/><circle cx="12" cy="10" r="2.2" fill="#fff"/></svg>
    </div>
  </div>

  <div class="contact-lines">
    <div class="holder">
      <p class="holder__name">ANNA KORIMA</p>
      <p class="holder__role">Sales Manager</p>
    </div>
    <p class="contact-line contact-line--phone">+64 9 571 3048</p>
    <p class="contact-line contact-line--fax">+64 9 571 6285</p>
    <p class="contact-line contact-line--mail">sales@falconfreight.example.nz</p>
    <p class="contact-line contact-line--address">12-18 Kowhai Lane, Ardmore, 2582<br>PO Box 814, Ardmore, Auckland 2583,<br>New Zealand</p>
  </div>
</section>

<section class="card card--back" aria-label="Business card back">
  <div class="back-layout">
    <div class="wordmark">
      <span class="wordmark__square"></span>
      <span class="wordmark__name">FALCON FREIGHT</span>
    </div>
    <p class="website">
      <svg viewBox="0 0 24 24" fill="none" stroke="#33a6d7" stroke-width="1.5"><circle cx="12" cy="12" r="10"/><ellipse cx="12" cy="12" rx="4.5" ry="10"/><path d="M2 12h20M4 7h16M4 17h16"/></svg>
      www.falconfreight.example.nz
    </p>
  </div>
</section>

</body>
</html>
```